Coffee House With Cycling Theme Wants Business Cards

We want to create a business card for a coffee house that has a cycling theme. We expect to use the current logo on one side of the business card and we have been considering adding the words 'COFFEE HOUSE' underneath (see example). For the other side of the business card we want an interesting design with tag-line, address and social media links (the normal business card stuff). See examples provided but we are not fixed on having it exactly as shown, we are very open to great creative ideas. Please note our logo has the initials ‘RM' in orange embedded in the design and this must be retained. However, you can play with the words COFFEE HOUSE as well as use the orange color on the backside of the business card, as you see fit. For an image on the backside of the business card it can be a photo, hand-drawn or whatever but it must visually combine coffee and cycling in some way. The interior of the Coffee House will be reclaimed wood, rustic and have an urban feel to it with cycling artifacts hanging from the walls/ceiling, etc. Finally, it would be beneficial if the business card design elements can be easily used on flyers and other promotional assets. Good luck, we are looking forward to seeing your creative ideas.

Target Market(s)

Coffee lovers and cycling fans

Contact Information for Business Card

See project description.

Colors

Designer to choose colors to be used in the design.

Requirements
Must have
• Must use the current logo provided and combine a coffee and bike theme.
Nice to have
• Orange is used in current logo and could be used as an accent color on the backside of the business card.

```html
<!DOCTYPE html>
<html lang="en">
<head>
<meta charset="utf-8">
<title>RM Coffee House – Business Cards</title>
<link href="https://fonts.googleapis.com/css2?family=Montserrat:wght@400;700&family=Pinyon+Script&display=swap" rel="stylesheet">
<style>
  :root {
    --page: #e4e4e2;
    --card-dark: #231f20;
    --band: #3b3a39;
    --orange: #ee5a24;
    --orange-deep: #c94d1f;
    --text-light: #d8d4d0;
    --icon-dark: #111;
  }
  html, body {
    margin: 0;
    width: 1200px;
    height: 675px;
    overflow: hidden;
    background: var(--page);
  }
  .canvas {
    position: relative;
    width: 1200px;
    height: 675px;
  }
  .card {
    position: absolute;
    top: 194px;
    width: 500px;
    height: 286px;
    background: var(--card-dark);
    overflow: hidden;
    box-shadow: 0 6px 18px rgba(0,0,0,0.25);
    font-family: "Montserrat", sans-serif;
  }
  .card--back { left: 70px; }
  .card--front { left: 630px; }

  /* Back side */
  .accent-panel {
    position: absolute;
    left: 0; top: 0;
    width: 245px; height: 100%;
    background: var(--orange);
  }
  .cup-illustration {
    position: absolute;
    left: 55px; top: 112px;
    width: 150px; height: 138px;
    border-radius: 6px;
    background: var(--orange-deep);
  }
  .tag-band {
    position: absolute;
    left: 0; top: 40px;
    width: 100%; height: 58px;
    background: var(--band);
  }
  .tagline {
    position: absolute;
    left: 18px; top: 44px;
    margin: 0;
    font-family: "Pinyon Script", cursive;
    font-size: 34px;
    font-weight: 400;
    color: var(--orange);
    line-height: 50px;
  }
  .business-name {
    position: absolute;
    right: 24px; top: 59px;
    margin: 0;
    font-size: 19px;
    font-weight: 700;
    letter-spacing: 1.5px;
    color: var(--orange);
  }
  .address {
    position: absolute;
    left: 300px; top: 150px;
    margin: 0;
    font-style: normal;
    font-size: 10px;
    line-height: 15px;
    letter-spacing: 0.5px;
    color: var(--text-light);
  }
  .social-links {
    position: absolute;
    left: 0; bottom: 22px;
    width: 100%;
    margin: 0; padding: 0 22px;
    box-sizing: border-box;
    list-style: none;
    display: flex;
    justify-content: space-between;
    font-size: 9px;
    color: var(--text-light);
  }
  .social-links li {
    display: flex;
    align-items: center;
    gap: 6px;
  }
  .social-dot {
    width: 14px; height: 14px;
    border-radius: 50%;
    background: var(--icon-dark);
    border: 1px solid #555;
  }
  .social-links li:first-child { color: #333; }

  /* Front side */
  .brand-name {
    position: absolute;
    left: 0; top: 0;
    width: 100%; height: 100%;
    margin: 0;
    display: flex;
    align-items: center;
    justify-content: center;
    gap: 12px;
    font-size: 34px;
    font-weight: 700;
    color: var(--orange);
  }
  .brand-mark {
    width: 18px; height: 18px;
    border-radius: 50%;
    background: var(--orange);
  }
</style>
</head>
<body>
<main class="canvas">
  <section class="card card--back" aria-label="Business card back">
    <div class="accent-panel"></div>
    <div class="cup-illustration" role="img" aria-label="Steaming coffee cup built from small coffee and cycling icons"></div>
    <div class="tag-band"></div>
    <h2 class="tagline">Your Tag Line</h2>
    <h1 class="business-name">COFFEE HOUSE</h1>
    <address class="address">
      Street Address<br>
      Street Address<br>
      Street Address
    </address>
    <ul class="social-links">
      <li><span class="social-dot"></span>rmcoffeehouse</li>
      <li><span class="social-dot"></span>rmcoffeehouse.com</li>
      <li><span class="social-dot"></span>rmcoffeehouse</li>
    </ul>
  </section>

  <section class="card card--front" aria-label="Business card front">
    <p class="brand-name"><span class="brand-mark"></span>RM Coffee House</p>
  </section>
</main>
</body>
</html>
```